Football blog needs a Wordpress design new site

We need a wordpress design for a new football blog site. We would like to see a design that uses the colours green, white and black and one that makes good use of the slideshow widgets as scene in the site 'www.tarnwick.net'
We would like a modern and sleek looking site but one that is also professional and easy to navigate.
Unfortunately due to unforeseen circumstances we are having to shorten the deadline date for this project.
The new deadline date is 16/07/2014.
We apologise for any inconveniance
Industry/Entity Type
It Professional
Look and feel

```html
<!DOCTYPE html>
<html lang="en">
<head>
<meta charset="utf-8">
<title>Sideline Chatter – Football Blog</title>
<link href="https://fonts.googleapis.com/css2?family=Source+Sans+3:wght@400;600;700&display=swap" rel="stylesheet">
<style>
:root{
  --grass-a:#3e8d24;
  --grass-b:#56a836;
  --green:#3fcf3a;
  --green-text:#2bb52a;
  --black:#000;
  --dark:#111;
  --forest:#062b0d;
  --forest-2:#031f08;
  --white:#fff;
  --grey:#666;
  --light:#ddd;
}
*{box-sizing:border-box;margin:0;padding:0}
html,body{width:805px;height:1200px;overflow:hidden}
body{
  position:relative;
  font-family:"Source Sans 3",sans-serif;
  color:var(--white);
  background:repeating-linear-gradient(90deg,var(--grass-a) 0 38px,var(--grass-b) 38px 76px);
}
a{color:inherit;text-decoration:none}
.abs{position:absolute}

/* header */
.brand{left:116px;top:54px;width:260px;height:46px;background:var(--white);display:flex;align-items:center;padding-left:6px;gap:6px}
.brand-dot{width:30px;height:30px;border-radius:50%;background:var(--green-text);position:absolute;left:22px;top:-46px;border:3px solid var(--white)}
.brand-name{font-size:33px;font-weight:600;color:var(--green-text);letter-spacing:-.5px}
.util{right:115px;top:12px;font-size:8px;display:flex;gap:6px;align-items:center}
.util .sq{width:9px;height:9px;border-radius:50%;background:var(--white);display:inline-block;margin-left:3px}
.topnav{right:115px;top:43px;font-size:8px;display:flex;gap:13px;text-transform:uppercase}
.search{left:497px;top:75px;width:193px;height:22px;display:flex}
.search span{flex:1;background:var(--white);color:var(--grey);font-size:8px;padding:6px}
.search b{width:22px;background:var(--green-text);display:flex;align-items:center;justify-content:center}

.mainnav{left:114px;top:114px;width:576px;height:34px;background:linear-gradient(#333,#0c0c0c);display:flex;align-items:center;font-size:8.5px;text-transform:uppercase}
.mainnav a{position:absolute}
.mainnav .on{color:var(--green)}

/* slider */
.slider{left:114px;top:150px;width:576px;height:265px;background:var(--dark)}
.hero{left:117px;top:154px;width:368px;height:206px;background:linear-gradient(160deg,#c9c9c4,#8b8a7e 45%,#4e6b2c 80%,#375a1e)}
.caption{left:117px;top:360px;width:321px;height:50px;padding:8px 7px}
.caption h2{font-size:10.5px;font-weight:700;margin-bottom:4px}
.caption p{font-size:7px;line-height:1.45}
.more{left:438px;top:365px;width:45px;height:44px;background:var(--green);font-size:13px;display:flex;align-items:center;justify-content:center}
.slide{left:490px;width:200px;height:64px;background:#000}
.slide .txt{position:absolute;left:10px;top:10px;width:92px}
.date{color:var(--green);font-size:7px}
.slide h3{font-size:7px;font-weight:700;margin:3px 0 4px}
.slide p{font-size:7px;line-height:1.4}
.slide .thumb{position:absolute;right:4px;top:2px;width:92px;height:60px}

/* must read */
.must{left:114px;top:416px;width:576px;height:211px;background:var(--white);color:#333}
.must h2{position:absolute;left:11px;top:10px;font-size:17px;font-weight:400}
.card{position:absolute;top:36px;width:132px}
.card .pic{height:92px;border:2px solid #ddd}
.card .date{color:var(--green-text);margin-top:10px}
.card h4{font-size:7px;font-weight:700;margin:4px 0 3px}
.card p{font-size:7px;line-height:1.5;color:var(--grey)}
.card .rm{font-size:7px;color:var(--green-text);margin-top:2px}

/* dark section */
.blackzone{left:114px;top:636px;width:576px;height:338px;background:var(--black)}
.post{left:116px;width:322px;height:100px;background:var(--white);color:#444}
.post .pic{position:absolute;left:6px;top:8px;width:94px;height:85px}
.post .body{position:absolute;left:113px;top:10px;width:200px}
.post h3{font-size:9.5px;font-weight:600;color:#555}
.post .meta{font-size:7px;margin:3px 0 5px}
.post p{font-size:7px;line-height:1.45;color:var(--grey)}
.post .rm{font-size:7px;color:var(--green-text);margin-top:2px}
.side-h{font-size:17px;font-weight:400}
.news{left:455px;width:230px}
.news .meta{color:var(--green);font-size:7px;margin-bottom:4px}
.news p{font-size:6.5px;line-height:1.55}
.articles{left:458px;top:870px;width:225px;font-size:7px;list-style:none}
.articles li{height:21px;white-space:nowrap;overflow:hidden}
.articles li::before{content:"➜";font-size:6px;margin-right:6px}
.articles li:first-child{color:var(--green)}

/* footer */
.footer{left:114px;top:974px;width:576px;height:164px;background:var(--forest)}
.fh{font-size:13.5px;font-weight:400}
.rp{left:135px;width:260px}
.rp .pic{position:absolute;left:0;top:0;width:54px;height:40px;background:linear-gradient(#6a8fb5,#8a7a5a 50%,#3d6a2c);border:2px solid #444}
.rp h4{position:absolute;left:59px;top:0;font-size:9.5px;font-weight:700;white-space:nowrap}
.rp p{position:absolute;left:59px;top:14px;font-size:6.5px;line-height:1.55;width:200px}
.about{left:436px;top:1027px;width:235px;font-size:7px;line-height:1.5}
.social{left:436px;top:1105px;display:flex;gap:11px}
.social span{width:13px;height:13px;border-radius:50%;background:var(--white)}
.bottombar{left:114px;top:1138px;width:576px;height:36px;background:var(--forest-2)}
.fbrand{left:138px;top:1145px}
.fbrand .row{display:flex;align-items:center;gap:4px;font-size:12px;font-weight:600;color:var(--green)}
.fbrand .row i{width:13px;height:13px;border-radius:50%;background:var(--white);display:inline-block}
.fbrand small{display:block;font-size:7px;color:var(--white);margin-left:19px}
.fnav{right:134px;top:1152px;display:flex;gap:9px;font-size:8px;text-transform:uppercase}
.fnav .on{color:var(--green)}
</style>
</head>
<body>

<header>
  <div class="abs brand"><span class="brand-dot"></span><span class="brand-name">Sideline Chatter</span></div>
  <div class="abs util"><span>New User?</span><a>Register</a><a>Login</a><a>Help</a>
    <span class="sq"></span><span class="sq"></span><span class="sq"></span><span class="sq"></span></div>
  <nav class="abs topnav"><a>News</a><a>Races</a><a>Results</a><a>Gallery</a><a>Video</a><a>Teams &amp; Coaches</a></nav>
  <div class="abs search"><span>Search...</span><b>
    <svg width="11" height="11" viewBox="0 0 12 12"><circle cx="5" cy="5" r="3.5" fill="none" stroke="#fff" stroke-width="1.5"/><line x1="7.6" y1="7.6" x2="11" y2="11" stroke="#fff" stroke-width="1.8"/></svg></b></div>
  <nav class="abs mainnav">
    <a class="on" style="left:20px">Home</a><a style="left:79px">Our Forum</a><a style="left:160px">News</a>
    <a style="left:219px">Blogs</a><a style="left:280px">Solutions</a><a style="left:358px">Advanced Search</a>
  </nav>
</header>

<section>
  <div class="abs slider"></div>
  <div class="abs hero" role="img" aria-label="Goalkeeper diving to save a shot in a packed stadium"></div>
  <div class="abs caption">
    <h2>Curabitur venenatis nisi scelerisque, consectetur nisi euismod,</h2>
    <p>Sed laoreet viverra tortor, vitae lacinia turpis consequat sit amet. Donec faucibus, leo vel ulla-mcorper cursus, arcu massa ultrices mi, non viverra sapien tellus et mi. Phasellus tempor ut</p>
  </div>
  <a class="abs more">More</a>

  <div class="abs slide" style="top:154px"><div class="txt"><div class="date">July 28,2014</div><h3>ELIPPORY TENDORRETY</h3><p>Proin bibendum, velit eu venenatis aliquam, massa</p></div><div class="thumb" role="img" aria-label="Goalkeeper stretching for the ball" style="background:linear-gradient(#9ab,#d8b64a 60%,#5a7d33)"></div></div>
  <div class="abs slide" style="top:220px"><div class="txt"><div class="date">July 28,2014</div><h3>ELIPPORY TENDORRETY</h3><p>Proin bibendum, velit eu venenatis aliquam, massa</p></div><div class="thumb" role="img" aria-label="Flag-painted ball on the pitch" style="background:linear-gradient(#2b3a4a,#4c7a2c 55%,#9cbc4a)"></div></div>
  <div class="abs slide" style="top:286px"><div class="txt"><div class="date">July 28,2014</div><h3>ELIPPORY TENDORRETY</h3><p>Proin bibendum, velit eu venenatis aliquam, massa</p></div><div class="thumb" role="img" aria-label="Player celebrating in front of the crowd" style="background:linear-gradient(#263a25,#3f6d2a 50%,#b33a1c)"></div></div>
  <div class="abs slide" style="top:352px"><div class="txt"><div class="date">July 28,2014</div><h3>ELIPPORY TENDORRETY</h3><p>Proin bibendum, velit eu venenatis aliquam, massa</p></div><div class="thumb" role="img" aria-label="Players contesting the ball in a match" style="background:linear-gradient(#3a4a55,#a33328 50%,#4b7a2e)"></div></div>
</section>

<section class="abs must">
  <h2>Must Read</h2>
  <div class="card" style="left:10px"><div class="pic" role="img" aria-label="Player sliding on the grass" style="background:linear-gradient(#2e4a2a,#6f8f52 45%,#c9cfc9 65%,#4d7a2f)"></div><div class="date">July 28,2014</div><h4>ELIPPORY TENDORRETY</h4><p>Proin bibendum, velit eu vene dfnatis aliquam, massa lorem sagittis ipsum,</p><div class="rm">Read More</div></div>
  <div class="card" style="left:217px;left:152px"><div class="pic" role="img" aria-label="Player in yellow shirt sitting on the pitch" style="background:linear-gradient(#c9ccd4,#8b9a7a 40%,#e6c92a 60%,#5a8a34)"></div><div class="date">July 28,2014</div><h4>ELIPPORY TENDORRETY</h4><p>Proin bibendum, velit eu vene dfnatis aliquam, massa lorem sagittis ipsum,</p><div class="rm">Read More</div></div>
  <div class="card" style="left:293px"><div class="pic" role="img" aria-label="Player striking the ball" style="background:linear-gradient(#d9d9d9,#b04a44 35%,#3f7a2a 70%,#2a5a1c)"></div><div class="date">July 28,2014</div><h4>ELIPPORY TENDORRETY</h4><p>Proin bibendum, velit eu vene dfnatis aliquam, massa lorem sagittis ipsum,</p><div class="rm">Read More</div></div>
  <div class="card" style="left:434px"><div class="pic" role="img" aria-label="Player in red kicking on a green field" style="background:linear-gradient(#a9b98a,#c43a2c 45%,#5f9a3a 70%)"></div><div class="date">July 28,2014</div><h4>ELIPPORY TENDORRETY</h4><p>Proin bibendum, velit eu vene dfnatis aliquam, massa lorem sagittis ipsum,</p><div class="rm">Read More</div></div>
</section>

<section>
  <div class="abs blackzone"></div>

  <article class="abs post" style="top:650px"><div class="pic" role="img" aria-label="Flares burning in the stands" style="background:radial-gradient(circle at 50% 50%,#e8453a,#7a1a1a 55%,#1a0a0a)"></div><div class="body"><h3>Proin metus magna, pharetra</h3><div class="meta">July 28, 2014 | 5 Comments | By Admin</div><p>Curabitur viverra neque nec urna blandit vulputate. Sed fringilla pellentesque nisl non iaculis. Vestibulum ante ipsum primis in faucibus orci luctus et ultrices posuere cubilia Curae; In vel vehicula quam. Pellentesque sodales</p><div class="rm">Read More</div></div></article>
  <article class="abs post" style="top:756px"><div class="pic" role="img" aria-label="Supporters cheering in blue shirts" style="background:linear-gradient(#1d2c4a,#3a5a9a 50%,#c7c9d6)"></div><div class="body"><h3>Proin metus magna, pharetra</h3><div class="meta">July 28, 2014 | 5 Comments | By Admin</div><p>Curabitur viverra neque nec urna blandit vulputate. Sed fringilla pellentesque nisl non iaculis. Vestibulum ante ipsum primis in faucibus orci luctus et ultrices posuere cubilia Curae; In vel vehicula quam. Pellentesque sodales</p><div class="rm">Read More</div></div></article>
  <article class="abs post" style="top:862px"><div class="pic" role="img" aria-label="Gloved hand above a ball on the grass" style="background:linear-gradient(#f2f2f2,#d8dde2 50%,#5aa032)"></div><div class="body"><h3>Proin metus magna, pharetra</h3><div class="meta">July 28, 2014 | 5 Comments | By Admin</div><p>Curabitur viverra neque nec urna blandit vulputate. Sed fringilla pellentesque nisl non iaculis. Vestibulum ante ipsum primis in faucibus orci luctus et ultrices posuere cubilia Curae; In vel vehicula quam. Pellentesque sodales</p><div class="rm">Read More</div></div></article>

  <h2 class="abs side-h" style="left:455px;top:646px">Recent News</h2>
  <div class="abs news" style="top:670px"><div class="meta">July 28, 2014 | 5 COMMENTS | By Admin</div><p>Nulla varius lacus nisl, ut tincidunt odio suscipit quis. Nulla facilisi. Nullam lacinia quis turpis et dignissim. Cras iaculis aliquam mauris, eu imperdiet dui venenatis ut.</p></div>
  <div class="abs news" style="top:725px"><div class="meta">July 28, 2014 | 5 COMMENTS | By Admin</div><p>Nulla varius lacus nisl, ut tincidunt odio suscipit quis. Nulla facilisi. Nullam lacinia quis turpis et dignissim. Cras iaculis aliquam mauris, eu imperdiet dui venenatis ut.</p></div>
  <div class="abs news" style="top:780px"><div class="meta">July 28, 2014 | 5 COMMENTS | By Admin</div><p>Nulla varius lacus nisl, ut tincidunt odio suscipit quis. Nulla facilisi. Nullam lacinia quis turpis et dignissim. Cras iaculis aliquam mauris, eu imperdiet dui venenatis ut.</p></div>

  <h2 class="abs side-h" style="left:455px;top:841px">Recent Articles</h2>
  <ul class="abs articles">
    <li>Cras hendrerit porttitor nisi vitae pellentesque. Pellentesque in</li>
    <li>Posuere est, ac placerat augue. Curabitur ullamcorper purus a</li>
    <li>Orci consectetur faucibus. Phasellus pretium ante in mi tincid-</li>
    <li>Unt, at malesuada neque venenatis. Cras scelerisque, sem non</li>
    <li>Wccumsan commodo, urna ipsum imperdiet arcu, eget euis-</li>
  </ul>
</section>

<footer>
  <div class="abs footer"></div>
  <h2 class="abs fh" style="left:135px;top:1000px">Recent Post</h2>
  <div class="abs rp" style="top:1025px"><div class="pic" role="img" aria-label="Stadium seen from the stands"></div><h4>Proin metus magna, pharetra</h4><p>Nulla varius lacus nisl, ut tincidunt odio suscipit quis. Nulla facilisi. Nullam lacinia quis turpis et dignissim. Cras iaculis aliquam mauris,</p></div>
  <div class="abs rp" style="top:1076px"><div class="pic" role="img" aria-label="Match action in front of goal"></div><h4>Proin metus magna, pharetra</h4><p>Nulla varius lacus nisl, ut tincidunt odio suscipit quis. Nulla facilisi. Nullam lacinia quis turpis et dignissim. Cras iaculis aliquam mauris,</p></div>

  <h2 class="abs fh" style="left:436px;top:1000px">About Sideline Chatter</h2>
  <p class="abs about">Lorem ipsum dolor sit amet, consectetur adipiscing elit. Ut porttitor elit justo, quis varius enim egestas id. Cras eget venenatis dui. Sed vel lectus augue. Maecenas eleifend elementum aliquam. Fusce eu lectus adipiscing, mattis dolor tempus, dictum massa.</p>
  <h2 class="abs fh" style="left:436px;top:1075px">Social Media</h2>
  <div class="abs social"><span></span><span></span><span></span><span></span></div>

  <div class="abs bottombar"></div>
  <div class="abs fbrand"><div class="row"><i></i>Sideline Chatter</div><small>© 2014 Privacy Policy</small></div>
  <nav class="abs fnav"><a class="on">Home</a><a>Our Forum</a><a>News</a><a>Blogs</a><a>Solutions</a><a>Advanced Search</a></nav>
</footer>

</body>
</html>
```